Need Letterhead Design & Matching Business Card

I have a logo that I love already. But the letterhead is less than appealing and boring. I'd like a design for my letterhead which I will match with business cards. Also, I'd like to have used fonts that are generally available, as my current letterhead uses a font named "SPACE" which nobody has unless they download it...so when a Word version is forwarded, it looks awful on the receiver's screed due to not having the font. That being said, modern is the look we like and are going for.

My business is "Halloran Brightmoor PC" - a law firm specializing in representing people who have suffered catastrophic injuries or death (plane, auto, train crashes etc.).

See attached letterhead, which has all of the pertinent information. My logo is also attached in various formats.

```html
<!DOCTYPE html>
<html lang="en">
<head>
<meta charset="utf-8">
<title>Halloran Brightmoor PC — Letterhead</title>
<link href="https://fonts.googleapis.com/css2?family=Raleway:wght@300;400;500;700&family=Allura&display=swap" rel="stylesheet">
<style>
  :root {
    --backdrop: #f1f1f1;
    --paper: #ffffff;
    --ink: #1a1a1a;
    --ink-strong: #333333;
    --ink-soft: #555555;
    --rule: #222222;
  }
  * { box-sizing: border-box; margin: 0; padding: 0; }
  html, body {
    width: 1200px; height: 1200px; overflow: hidden;
    background: var(--backdrop);
    font-family: "Raleway", Arial, sans-serif;
    color: var(--ink);
  }
  .letterhead {
    position: absolute; left: 225px; top: 117px;
    width: 750px; height: 966px;
    background: var(--paper);
  }
  .brand {
    position: absolute; top: 42px; left: 0; right: 0;
    display: flex; justify-content: center; align-items: center; gap: 16px;
  }
  .brand-square { width: 40px; height: 40px; background: var(--ink); }
  .brand-name {
    font-weight: 300; font-size: 38px; letter-spacing: 1px;
    color: var(--ink); text-transform: uppercase; line-height: 1;
  }
  .recipient { position: absolute; left: 68px; top: 210px; width: 614px; }
  .recipient-name { font-weight: 700; font-size: 18px; color: var(--ink-strong); margin-bottom: 8px; }
  .recipient-line { font-size: 11px; line-height: 17.8px; color: var(--ink-soft); }
  .letter-date {
    position: absolute; right: 0; bottom: 0;
    font-size: 11px; line-height: 17.8px; color: var(--ink-soft);
  }
  .letter-body {
    position: absolute; left: 68px; top: 345px; width: 616px;
    font-size: 11.3px; line-height: 17.6px; color: var(--ink-soft);
    text-align: justify;
  }
  .letter-body p + p { margin-top: 17.6px; }
  .sign-off { position: absolute; left: 68px; top: 722px; }
  .signature { font-family: "Allura", cursive; font-size: 34px; color: var(--ink); line-height: 1; }
  .signer-name { font-weight: 700; font-size: 16px; color: var(--ink-strong); margin-top: 2px; }
  .signer-title { font-size: 11px; color: var(--ink-soft); margin-top: 4px; }
  .footer {
    position: absolute; left: 0; right: 0; top: 898px;
    display: flex; justify-content: center; align-items: stretch;
    font-size: 10.5px; font-weight: 700; line-height: 15px; color: var(--ink);
  }
  .footer-address { text-align: right; padding-right: 16px; border-right: 1.5px solid var(--rule); }
  .footer-contact { padding-left: 16px; }
  .contact-row { display: flex; align-items: center; gap: 9px; }
  .contact-row svg { width: 9px; height: 9px; fill: var(--ink); flex: none; }
</style>
</head>
<body>
  <main class="letterhead">
    <header class="brand">
      <span class="brand-square"></span>
      <span class="brand-name">Halloran Brightmoor PC</span>
    </header>

    <section class="recipient">
      <p class="recipient-name">Name Surname</p>
      <p class="recipient-line">Senior Executive</p>
      <p class="recipient-line">Address goes here. Street, City, Country</p>
      <p class="recipient-line">contact@yourmail.com</p>
      <p class="recipient-line">000-987-654-321</p>
      <p class="letter-date">Date, 10 September, 2030</p>
    </section>

    <article class="letter-body">
      <p>Lorem ipsum dolor sit amet, consectetur adipisicing elit, sed do eiusmod tempor incididunt ut labore et dolore magna aliqua. Ut enim ad minim veniam, quis nostrud exercitation ullamco laboris nisi ut aliquip ex ea commodo consequat. Duis aute irure dolor in reprehenderit in voluptate velit esse cillum dolore eu fugiat nulla pariatur. Excepteur sint occaecat cupidatat non proident, sunt in culpa qui officia deserunt mollit anim id est laborum. Sed ut perspiciatis unde omnis iste natus error sit voluptatem accusantium doloremque laudantium, totam rem aperiam, eaque ipsa quae ab illo inventore veritatis et quasi architecto beatae vitae dicta sunt explicabo. Nemo enim ipsam voluptatem quia voluptas sit aspernatur aut odit aut fugit, sed quia consequuntur magni dolores eos qui ratione voluptatem sequi nesciunt. Neque porro voluptatem sequi nesciunt. Nemo enim ipsam voluptatem quia voluptas.</p>
      <p>Lorem ipsum dolor sit amet, consectetur adipisicing elit, sed do eiusmod tempor incididunt ut labore et dolore magna aliqua. Ut enim ad minim veniam, quis nostrud exercitation ullamco laboris nisi ut aliquip ex ea commodo consequat. Duis aute irure dolor in reprehenderit in voluptate velit esse cillum dolore eu fugiat nulla pariatur. Excepteur sint occaecat cupidatat non proident, sunt in culpa qui officia deserunt mollit anim id est laborum. Sed ut perspiciatis unde omnis iste natus error sit voluptatem accusantium doloremque laudantium, totam rem aperiam, eaque ipsa quae ab illo inventore veritatis et quasi architecto beatae vitae dicta sunt explicabo. Nemo enim ipsam voluptatem quia voluptas sit aspernatur aut odit aut.</p>
      <p>Lorem ipsum dolor sit amet, consectetur adipisicing elit, sed do eiusmod tempor incididunt ut labore et dolore magna aliqua. Ut enim ad minim veniam, quis nostrud exercitation ullamco laboris nisi ut aliquip ex ea commodo consequat. .</p>
    </article>

    <section class="sign-off">
      <p class="signature">Namesurname</p>
      <p class="signer-name">NAME SURNAME</p>
      <p class="signer-title">General Manager</p>
    </section>

    <footer class="footer">
      <div class="footer-address">
        <p>R. Devin Castellan, Esq. | President</p>
        <p>4820 Larchmont Ave. | suite 300</p>
        <p>Easton Park, CA 90418</p>
      </div>
      <div class="footer-contact">
        <p class="contact-row">
          <svg viewBox="0 0 10 10" aria-hidden="true"><path d="M0 2h10v6H0z M0 2l5 3.5L10 2" fill="none" stroke="#1a1a1a" stroke-width="1.2"/></svg>
          rdc@halloranbrightmoor.com
        </p>
        <p class="contact-row">
          <svg viewBox="0 0 10 10" aria-hidden="true"><circle cx="5" cy="5" r="4.3" fill="none" stroke="#1a1a1a" stroke-width="1.1"/><path d="M0.7 5h8.6M5 0.7c-2.4 2.6-2.4 6 0 8.6M5 0.7c2.4 2.6 2.4 6 0 8.6" fill="none" stroke="#1a1a1a" stroke-width="0.9"/></svg>
          www.halloranbrightmoor.com
        </p>
        <p class="contact-row">
          <svg viewBox="0 0 10 10" aria-hidden="true"><path d="M2.2 0.5l1.8 2.2-1 1.2c.6 1.3 1.7 2.4 3 3l1.2-1 2.3 1.8-.9 1.6c-.4.4-1 .5-1.6.3C4 8.4 1.6 6 .4 2.9.2 2.3.3 1.7.7 1.3z"/></svg>
          (855) 555-0142
        </p>
      </div>
    </footer>
  </main>
</body>
</html>
```